New Business Cards for KM&DR

We need updated business cards for a staff of 15 engineers, estimators, project managers, and sales people. We have recently begun changes to our website and marketing material to improve our look and branding. We are an established fabricator specializing in pressure vessels, tanks, and structural steel. The owners require us to use the existing logo and old english text design. Also, we prefer dark grey or mostly black cards.
Target Market(s)
Engineers, purchasing agents, estimators, and project managers of; mining companies, refineries, industrial construction professionals
Industry/Entity Type
Business
Contact Information for Business Card
Logo, phone, website, email, etc.
Look and feel
Each slider illustrates characteristics of the customer's brand and the style your logo design should communicate.

```html
<!DOCTYPE html>
<html lang="en">
<head>
<meta charset="utf-8">
<title>KM&amp;DR Business Card</title>
<link href="https://fonts.googleapis.com/css2?family=Quattrocento:wght@400;700&display=swap" rel="stylesheet">
<style>
  :root {
    --backdrop: #dedede;
    --card-dark: #0d0d0d;
    --card-light: #f4f4f4;
    --ink-light: #f2f2f2;
    --ink-dark: #141414;
    --ink-muted: #3a3a3a;
  }
  * { margin: 0; padding: 0; box-sizing: border-box; }
  html, body {
    width: 1200px; height: 576px; overflow: hidden;
    background: var(--backdrop);
    font-family: "Quattrocento", Georgia, serif;
  }
  .canvas { position: relative; width: 1200px; height: 576px; }
  .card {
    position: absolute; top: 138px;
    width: 484px; height: 293px; border-radius: 14px;
  }
  .card--front { left: 82px; background: var(--card-dark); color: var(--ink-light); }
  .card--back { left: 602px; background: var(--card-light); color: var(--ink-dark); }

  .front-mark {
    position: absolute; left: 0; right: 0; top: 82px;
    display: flex; align-items: center; justify-content: center; gap: 14px;
  }
  .mark-dot { width: 34px; height: 34px; border-radius: 50%; background: var(--ink-light); }
  .mark-name { font-size: 44px; font-weight: 700; letter-spacing: 1px; color: var(--ink-light); }
  .front-company {
    position: absolute; left: 0; right: 0; top: 203px;
    text-align: center; font-size: 17px; letter-spacing: 0.3px;
  }

  .back-brand {
    position: absolute; right: 24px; top: 32px;
    display: flex; align-items: center; gap: 14px;
  }
  .back-mark { display: flex; align-items: center; gap: 8px; }
  .back-mark .mark-dot { width: 18px; height: 18px; background: var(--ink-dark); }
  .back-mark .mark-name { font-size: 22px; color: var(--ink-dark); letter-spacing: 0.5px; }
  .back-company { font-size: 22px; font-weight: 700; line-height: 27px; }

  .person { position: absolute; left: 26px; top: 155px; }
  .person-name { font-size: 20px; font-weight: 700; line-height: 24px; }
  .person-role { font-size: 11px; color: var(--ink-muted); margin-top: 1px; }

  .contacts {
    position: absolute; left: 26px; top: 204px;
    list-style: none; font-size: 12.5px; line-height: 17px;
  }
  .contacts li { display: flex; align-items: center; gap: 6px; }
  .icon { width: 11px; height: 11px; fill: var(--ink-dark); flex: none; margin-right: 7px; }
  .contacts .gap { margin-left: 6px; }
</style>
</head>
<body>
<div class="canvas">

  <section class="card card--front">
    <div class="front-mark">
      <span class="mark-dot"></span>
      <span class="mark-name">KM&amp;DR</span>
    </div>
    <p class="front-company">Kessler Metal &amp; Drum Rolling</p>
  </section>

  <section class="card card--back">
    <div class="back-brand">
      <div class="back-mark">
        <span class="mark-dot"></span>
        <span class="mark-name">KM&amp;DR</span>
      </div>
      <p class="back-company">Kessler Metal &amp;<br>Drum Rolling</p>
    </div>

    <div class="person">
      <h1 class="person-name">J. Harlan</h1>
      <p class="person-role">Director</p>
    </div>

    <ul class="contacts">
      <li>
        <svg class="icon" viewBox="0 0 12 12"><path d="M1 4c0-2 2-3 5-3s5 1 5 3H8.5V3h-5v1z M2.5 5h7l1 6h-9z"/></svg>
        801-555-0142
      </li>
      <li>
        <svg class="icon" viewBox="0 0 12 12"><path d="M3 1h6v3H3z M1 5h10v4H9v2H3V9H1z M4 8v2h4V8z" fill-rule="evenodd"/></svg>
        801-555-0178
      </li>
      <li>
        <svg class="icon" viewBox="0 0 12 12"><path d="M1 2.5h10v7H1z M1.5 3l4.5 4 4.5-4" fill="none" stroke="#141414" stroke-width="1.3"/></svg>
        harlan@kmanddr.com
        <svg class="icon gap" viewBox="0 0 12 12"><circle cx="6" cy="6" r="5" fill="none" stroke="#141414" stroke-width="1.1"/><path d="M1 6h10M6 1c-3 3-3 7 0 10M6 1c3 3 3 7 0 10" fill="none" stroke="#141414" stroke-width="1"/></svg>
        www.kmanddr.com
      </li>
      <li>
        <svg class="icon" viewBox="0 0 12 12"><path d="M6 .5a4 4 0 0 1 4 4c0 3-4 7-4 7s-4-4-4-7a4 4 0 0 1 4-4zm0 2.3a1.7 1.7 0 1 0 0 3.4 1.7 1.7 0 0 0 0-3.4z" fill-rule="evenodd"/></svg>
        480 Foundry Lane Riverton City 84065
      </li>
    </ul>
  </section>

</div>
</body>
</html>
```